Pop-up Banner

Would like a design for a pop-up 85 x 206cm banner for a trade show. (from norla press)
We would like "our logo" (brightwave holdings) - then the tagline - "Your Trusted Partner in Data-Driven Decisions"
*Supporting Bullets*
Unified data, analytics & AI
Trusted insights, faster outcomes
Real-time intelligence at scale
Enterprise-ready, secure solutions
Clarity from data complexity
trusted by...some company logos
Partners with : partner logo
Our Colours: #FFA300, #3D4176, #FDD16E, #F87C57, #A68118, #1C2F36

```html
<!DOCTYPE html>
<html lang="en">
<head>
<meta charset="utf-8">
<title>Brightwave Holdings – Pop-up Banner</title>
<link href="https://fonts.googleapis.com/css2?family=Poppins:wght@400;500;600;700&display=swap" rel="stylesheet">
<style>
  :root {
    --orange: #FF9A00;
    --orange-soft: #FFAE3A;
    --white: #FFFFFF;
    --stage: #EEEEEE;
    --label: #6F6F6F;
    --navy: #1C2F36;
    --indigo: #3D4176;
    --coral: #F87C57;
    --gold: #A68118;
    --teal: #137A78;
    --red: #C8102E;
    --green: #3DAA3D;
    --blue: #1A73C8;
  }
  * { margin: 0; padding: 0; box-sizing: border-box; }
  html, body {
    width: 1200px; height: 1162px; overflow: hidden;
    background: var(--stage);
    font-family: "Poppins", sans-serif;
  }
  .banner {
    position: absolute; left: 390px; top: 109px;
    width: 419px; height: 944px;
    background: var(--white);
    overflow: hidden;
    box-shadow: 0 6px 18px rgba(0,0,0,0.08);
  }
  .corner-arc { position: absolute; left: 0; top: 0; }
  .brand {
    position: absolute; left: 50px; top: 83px;
    display: flex; align-items: center; gap: 18px;
  }
  .brand-mark {
    width: 72px; height: 72px; border-radius: 50%;
    background: var(--orange);
  }
  .brand-name {
    color: var(--orange); font-weight: 700;
    font-size: 25px; line-height: 29px; letter-spacing: 0.3px;
  }
  .tagline {
    position: absolute; left: 0; right: 0; top: 210px;
    text-align: center; color: var(--orange);
    font-size: 14px; font-weight: 400;
  }
  .features {
    position: absolute; left: 0; top: 264px;
    width: 419px; height: 399px;
    background: var(--orange); overflow: hidden;
  }
  .features-sheen { position: absolute; left: 0; top: 0; }
  .feature {
    position: absolute; left: 76px;
    display: flex; align-items: center;
  }
  .feature-icon {
    width: 54px; height: 54px;
    border: 1.4px solid var(--white); border-radius: 2px;
    display: flex; align-items: center; justify-content: center;
    flex-shrink: 0;
  }
  .feature-text {
    margin-left: 34px; color: var(--white);
    font-size: 15.5px; line-height: 23px; letter-spacing: 0.5px;
  }
  .section-label {
    position: absolute; left: 0; right: 0;
    text-align: center; color: var(--label);
    font-size: 9px; letter-spacing: 0.6px; font-weight: 500;
  }
  .client {
    position: absolute; display: flex; align-items: center; gap: 5px;
    font-weight: 600; white-space: nowrap; transform: translate(-50%, -50%);
  }
  .dot { width: 22px; height: 22px; border-radius: 50%; }
  .square { width: 16px; height: 16px; }
</style>
</head>
<body>
<main class="banner">
  <svg class="corner-arc" width="419" height="264" viewBox="0 0 419 264" aria-hidden="true">
    <path d="M228 0 H419 V186 C370 90 300 30 228 0 Z" fill="var(--orange-soft)"/>
  </svg>

  <header class="brand">
    <div class="brand-mark"></div>
    <div class="brand-name">BRIGHTWAVE<br>HOLDINGS</div>
  </header>

  <p class="tagline">“Your Trusted Partner in Data-Driven Decisions”</p>

  <section class="features">
    <svg class="features-sheen" width="419" height="399" viewBox="0 0 419 399" aria-hidden="true">
      <path d="M225 0 H419 V100 C330 80 265 40 225 0 Z" fill="var(--orange-soft)" opacity="0.85"/>
    </svg>

    <div class="feature" style="top:31px">
      <div class="feature-icon">
        <svg width="20" height="20" viewBox="0 0 20 20" fill="none" stroke="#fff" stroke-width="1.2"><ellipse cx="10" cy="4" rx="7" ry="2.5"/><path d="M3 4v9c0 1.4 3.1 2.5 7 2.5s7-1.1 7-2.5V4M3 8.5c0 1.4 3.1 2.5 7 2.5s7-1.1 7-2.5"/></svg>
      </div>
      <p class="feature-text">Unified data, analytics<br>&amp; AI</p>
    </div>
    <div class="feature" style="top:102px">
      <div class="feature-icon">
        <svg width="20" height="20" viewBox="0 0 20 20" fill="none" stroke="#fff" stroke-width="1.2"><path d="M5 13a3.5 3.5 0 0 1 0-7 5 5 0 0 1 9.5 1A3 3 0 0 1 15 13"/><path d="M10 10v7M7 12v3M13 12v3"/></svg>
      </div>
      <p class="feature-text">Real-time intelligence<br>at scale</p>
    </div>
    <div class="feature" style="top:173px">
      <div class="feature-icon">
        <svg width="20" height="20" viewBox="0 0 20 20" fill="none" stroke="#fff" stroke-width="1.2"><path d="M3 8h14l-2 5H5z"/><path d="M7 4v4M10 3v5M13 4v4M10 13v4"/></svg>
      </div>
      <p class="feature-text">Clarity from data<br>complexity</p>
    </div>
    <div class="feature" style="top:244px">
      <div class="feature-icon">
        <svg width="22" height="20" viewBox="0 0 22 20" fill="none" stroke="#fff" stroke-width="1.2"><circle cx="12" cy="10" r="7"/><path d="M12 10l-3-3M1 9h5M2 12h4"/></svg>
      </div>
      <p class="feature-text">Trusted insights,<br>faster outcomes</p>
    </div>
    <div class="feature" style="top:315px">
      <div class="feature-icon">
        <svg width="20" height="20" viewBox="0 0 20 20" fill="none" stroke="#fff" stroke-width="1.2"><path d="M10 2l7 3v5c0 4-3 7-7 8-4-1-7-4-7-8V5z"/><path d="M6.5 10l2.5 2.5 4.5-5"/></svg>
      </div>
      <p class="feature-text">Enterprise-ready,<br>secure solutions</p>
    </div>
  </section>

  <p class="section-label" style="top:700px">TRUSTED BY</p>
  <div class="client" style="left:83px; top:736px; color:var(--indigo); font-size:17px"><span class="dot" style="background:var(--blue)"></span>Larkfield</div>
  <div class="client" style="left:212px; top:736px; color:#555; font-size:17px; font-weight:400">Quillo</div>
  <div class="client" style="left:333px; top:736px; color:var(--navy); font-size:17px; letter-spacing:1.5px">VANTORA</div>
  <div class="client" style="left:142px; top:773px; color:var(--teal); font-size:17px; font-weight:700">Meridyn</div>
  <div class="client" style="left:264px; top:773px; color:var(--navy); font-size:10px; font-weight:700"><span class="square" style="background:var(--red); width:22px; height:22px"></span>HARBOURGATE</div>

  <p class="section-label" style="top:834px">PARTNERS WITH</p>
  <div class="client" style="left:94px; top:862px; color:#555; font-size:14px; font-weight:500"><span class="square" style="background:var(--coral)"></span>Corvexa</div>
  <div class="client" style="left:213px; top:862px; color:var(--red); font-size:14px; letter-spacing:1px">STELLARO</div>
  <div class="client" style="left:341px; top:862px; color:#222; font-size:16px; font-weight:400">tallis</div>
  <div class="client" style="left:210px; top:891px; color:var(--blue); font-size:14px; font-weight:500"><span class="dot" style="background:var(--green); width:16px; height:16px"></span>ledgerpoint</div>
</main>
</body>
</html>
```